VELORA ARENA CHANNEL-Where being an athlete is a STATE OF MIND-NOT A GENDER

WEBSITE AND OTT NETWORK DEDICATED TO WOMENS SPORTS
VELORA ARENA CHANNEL intends to address the needs of this underserved market in women’s sports media coverage by uniquely delivering 24/7 focused coverage to those interested specifically in women’s sports and related stories, in a more direct and customer driven way.

Our product provides the following solutions:
1. Provides programming to an underserved market
2. Provides expansive exposure (a critical ingredient) for the success of professional women’s sports
3. Values the athletic achievement of female athletes

This will be accomplished in two phases:
Phase 1
Create a dynamic website dedicated to women’s sports featuring up to date scores, highlights and news.
Phase 2
1. Create a full-spectrum OTT (over the top) network that reflects the dynamic and changing nature of women’s athletics, providing innovative programming, helpful information, community and individual experiences, entertainment and a touch of much-needed humor.
2. Create a network dedicated to women’s sports and entertainment that features steady rotation of daily news and highlights of women’s sports delivered by a majority of women reporters. A sports channel for women by women.
3. To offer live, pre-taped, original and diverse programming 24 hours a day seven days a week, 365 days a year.

VVELORA ARENA CHANNEL website “ Veloratv.net “ fills a need to help women’s sports and entertainment enthusiasts get the complete array of scores and highlights they are craving to make the most of their viewing time online. Stats
So VeloraTV.net plans to go above and beyond what the current sports driven websites offer. But beyond what we will offer the consumer, we are also providing an incredible platform for women in sports to showcase their talent to a starved underserved crowd of sports fans.
No matter what your age or skill level or even education, people are searching the web to find specific information, products, and services that interest them. Recognizing the magnitude of our target market that are searching the Internet for various information we realize the importance of meeting their needs with opportunities to discover who we are and what we do. With every search, every click and every download we will be able to get one step closer to our target market.

Target Market(s)

people interested in womens sports

Number of Pages Required

4 page

Font styles to use
Serif

Requirements
Must have
• home page design exactly like www.brisklanegames.net and the ott page (watch page) similar to streamora page, all with womens sports in mind
Nice to have
• view brisklanegames and streamora. Color coordinate to logo

```html
<!DOCTYPE html>
<html lang="en">
<head>
<meta charset="utf-8">
<title>Velora Arena Channel</title>
<link href="https://fonts.googleapis.com/css2?family=Open+Sans:wght@400;600;700;800&display=swap" rel="stylesheet">
<style>
:root{
  --red:#d5232b;
  --orange:#ee5a24;
  --black:#111;
  --dark:#1f1f1f;
  --grey-band:#e6e6e6;
  --text:#444;
  --white:#fff;
}
*{box-sizing:border-box;margin:0;padding:0}
html,body{width:683px;height:1200px;overflow:hidden}
body{font-family:"Open Sans",sans-serif;background:var(--white);color:var(--text);position:relative}
.wrap{width:623px;margin:0 auto;position:relative}

.topbar{height:40px;background:var(--black)}
.topbar .wrap{display:flex;justify-content:space-between;align-items:center;height:40px}
.brand{display:flex;align-items:center;gap:6px;color:var(--red);font-weight:800;font-size:12px;letter-spacing:.5px}
.brand-dot{width:16px;height:16px;border-radius:50%;background:var(--red)}
.account{display:flex;align-items:center;gap:10px;color:var(--white);font-size:8px}
.account .sep{color:#777}
.social{display:flex;gap:5px;margin-left:14px}
.social span{width:13px;height:13px;background:#555;border-radius:2px}

.mainnav{height:16px;background:var(--red)}
.mainnav ul{list-style:none;display:flex;gap:18px;height:16px;align-items:center;font-size:7.5px;font-weight:600;color:var(--white)}

.hero{height:244px;position:relative;background:linear-gradient(180deg,#6d6f6a 0%,#8b2a2c 45%,#b32429 62%,#4c7d35 78%,#3d6b2a 100%)}
.hero .arrow{position:absolute;top:108px;width:22px;height:22px;border-radius:50%;background:rgba(0,0,0,.35)}
.hero .arrow.left{left:12px}.hero .arrow.right{right:12px}
.hero svg{position:absolute;top:5px;left:5px}

.today{height:18px;background:var(--dark);border-top:2px solid var(--orange)}
.today .wrap{display:flex;align-items:center;height:16px;font-size:7.5px;color:var(--white)}
.today-tab{background:var(--orange);height:20px;margin-top:-4px;padding:0 18px;display:flex;align-items:center;font-weight:700;font-size:10px;margin-right:10px}
.today .more{color:var(--orange);margin-left:4px}

.sport-tabs{margin-top:24px;height:18px;background:var(--dark);display:flex;align-items:center;font-size:7px;color:var(--white)}
.sport-tabs span{padding:0 8px;height:18px;display:flex;align-items:center}
.sport-tabs .active{background:var(--orange);font-weight:700}

.filter{height:95px;display:flex;justify-content:space-between;padding-top:10px}
.filter-left{display:flex;gap:12px}
.filter-tag{background:var(--orange);color:var(--white);font-size:8px;font-weight:700;height:14px;width:58px;padding-left:6px;display:flex;align-items:center}
.filter-title{color:var(--orange);font-weight:700;font-size:11px}
.options{display:grid;grid-template-columns:60px 70px;gap:3px 6px;margin-top:6px;font-size:6.5px}
.options label{display:flex;align-items:center;gap:3px}
.radio{width:6px;height:6px;border:1px solid #888;border-radius:50%}
.radio.on{background:#666}
.ad{width:310px;height:28px;background:#dfe6ee;display:flex;align-items:center;justify-content:space-between;padding:0 10px;font-size:9px;color:#1d3c6b}
.ad .ad-brand{font-weight:700}
.ad .ad-btn{background:#f2c230;color:#1d3c6b;font-size:7px;font-weight:700;padding:3px 8px;border-radius:2px}

.band{background:var(--grey-band);padding:20px 0}
.cards{display:grid;grid-template-columns:repeat(4,1fr);gap:10px}
.card{background:var(--white);border-bottom:2px solid var(--red);height:168px}
.card-photo{height:78px;background:linear-gradient(160deg,#9aa0a6,#c23a3e 55%,#2d3a4f)}
.card:nth-child(2) .card-photo{background:linear-gradient(160deg,#2f3f6f,#c9cbd2 60%,#7a1d25)}
.card:nth-child(3) .card-photo{background:linear-gradient(160deg,#d8d8d8,#8e8e8e 60%,#e2e2e2)}
.card:nth-child(4) .card-photo{background:linear-gradient(160deg,#b9783b,#3b2a22 55%,#7d8a92)}
.card h3{color:var(--red);font-size:7.5px;font-weight:800;padding:6px 6px 3px}
.card p{font-size:6.5px;line-height:1.45;padding:0 6px}

.section-title{height:66px;display:flex;align-items:flex-end;padding-bottom:12px;font-size:19px;font-weight:700;color:#222}
.gap{height:40px}

.footer{background:var(--black);border-top:3px solid var(--orange);height:175px}
.footer .wrap{display:flex;padding-top:16px}
.footer .brand{width:230px;align-items:flex-start}
.fcol{font-size:7px;color:#ccc;line-height:1.6}
.fcol h4{color:var(--orange);font-size:9px;font-weight:700;margin-bottom:2px}
.quick{display:flex;gap:36px;width:180px}
.join{width:140px}
.follow .social{margin-left:0;margin-top:4px}
.copyright{background:#050505;height:40px;display:flex;align-items:center;justify-content:center;font-size:6.5px;color:#aaa;border-top:1px solid #222}
</style>
</head>
<body>
<header class="topbar">
  <div class="wrap">
    <div class="brand"><span class="brand-dot"></span>VELORA ARENA CHANNEL</div>
    <div class="account"><span>Login</span><span class="sep">|</span><span>Register</span>
      <div class="social"><span></span><span></span><span></span></div>
    </div>
  </div>
</header>
<nav class="mainnav"><div class="wrap"><ul>
  <li>About Us</li><li>Watch</li><li>Programs</li><li>Sports</li><li>Schedule</li><li>Top Stories</li><li>Blogs</li><li>Videos</li><li>Contact Us</li>
</ul></div></nav>

<section class="hero" role="img" aria-label="Women's football team celebrating together on the pitch">
  <span class="arrow left"></span><span class="arrow right"></span>
</section>

<div class="today"><div class="wrap">
  <span class="today-tab">Today</span>
  <span>Wednesday Night Soccer: Ridgefield Storm FC v Marlow Heights FC ...</span><span class="more">Read more</span>
</div></div>

<div class="wrap">
  <div class="sport-tabs">
    <span class="active">All</span><span>Baseball</span><span>Basketball</span><span>Cricket</span><span>Car Sports</span><span>eSports</span><span>Golf</span><span>Hockey</span><span>Ice Hockey</span><span>MMA</span><span>Racquet Sports</span><span>Rugby</span><span>Soccer</span>
  </div>
  <div class="filter">
    <div class="filter-left">
      <div class="filter-tag">Filter</div>
      <div>
        <div class="filter-title">Baseball</div>
        <div class="options">
          <label><span class="radio on"></span>All</label><span></span>
          <label><span class="radio"></span>Live Now</label><label><span class="radio"></span>Plays Of The Week</label>
          <label><span class="radio"></span>Featured Videos</label><label><span class="radio"></span>Best Of 2015</label>
        </div>
      </div>
    </div>
    <div class="ad"><span class="ad-brand">Covella</span><span>15%.... need I say more?</span><span class="ad-btn">Start Quote</span></div>
  </div>
</div>

<section class="band"><div class="wrap cards">
  <article class="card"><div class="card-photo" role="img" aria-label="Baseball players on the field"></div><h3>EVENT HEAD LINE HERE</h3><p>Lena Varoux has informed Harbor City that she is not interested in leaving Castellan FC for the Premier Cup club, Mira Dunholt reports.</p></article>
  <article class="card"><div class="card-photo" role="img" aria-label="Hockey players on the ice"></div><h3>EVENT HEAD LINE HERE</h3><p>Lena Varoux has informed Harbor City that she is not interested in leaving Castellan FC for the Premier Cup club, Mira Dunholt reports.</p></article>
  <article class="card"><div class="card-photo" role="img" aria-label="Tennis player mid-serve"></div><h3>EVENT HEAD LINE HERE</h3><p>Lena Varoux has informed Harbor City that she is not interested in leaving Castellan FC for the Premier Cup club, Mira Dunholt reports.</p></article>
  <article class="card"><div class="card-photo" role="img" aria-label="Basketball player on court"></div><h3>EVENT HEAD LINE HERE</h3><p>Lena Varoux has informed Harbor City that she is not interested in leaving Castellan FC for the Premier Cup club, Mira Dunholt reports.</p></article>
</div></section>

<div class="wrap"><h2 class="section-title">Programs Exclusive To Velora</h2></div>

<section class="band"><div class="wrap cards">
  <article class="card"><div class="card-photo" role="img" aria-label="Football players in match action"></div><h3>EVENT HEAD LINE HERE</h3><p>Lena Varoux has informed Harbor City that she is not interested in leaving Castellan FC for the Premier Cup club, Mira Dunholt reports.</p></article>
  <article class="card"><div class="card-photo" role="img" aria-label="Hockey team at the rink"></div><h3>EVENT HEAD LINE HERE</h3><p>Lena Varoux has informed Harbor City that she is not interested in leaving Castellan FC for the Premier Cup club, Mira Dunholt reports.</p></article>
  <article class="card"><div class="card-photo" role="img" aria-label="Tennis match on court"></div><h3>EVENT HEAD LINE HERE</h3><p>Lena Varoux has informed Harbor City that she is not interested in leaving Castellan FC for the Premier Cup club, Mira Dunholt reports.</p></article>
  <article class="card"><div class="card-photo" role="img" aria-label="Basketball game in arena"></div><h3>EVENT HEAD LINE HERE</h3><p>Lena Varoux has informed Harbor City that she is not interested in leaving Castellan FC for the Premier Cup club, Mira Dunholt reports.</p></article>
</div></section>

<div class="gap"></div>

<footer>
  <div class="footer"><div class="wrap">
    <div class="brand"><span class="brand-dot"></span>VELORA ARENA CHANNEL</div>
    <div class="quick">
      <div class="fcol"><h4>Quick Links</h4>Home<br>About Us<br>Watch<br>Programs<br>Sports<br>Schedule</div>
      <div class="fcol"><h4>&nbsp;</h4>Top Stories<br>Blogs<br>Videos<br>Contact Us<br>Privacy Policy<br>Site Map</div>
    </div>
    <div class="fcol join"><h4>Join Us</h4>Login<br>Register</div>
    <div class="fcol follow"><h4>Follow Us</h4><div class="social"><span></span><span></span><span></span></div></div>
  </div></div>
  <div class="copyright">COPYRIGHT © 2015 Velora &nbsp;|&nbsp; All rights are reserved</div>
</footer>
</body>
</html>
```